Kestrel Golf Circle Chart

I would like some type of design that can then be used on our website, like a png. or .jpeg or vector format. We want a circle/flow chart that describes our golf coaching process and has our logo faded in the background. attached is a rough draft to give you a general idea..something I created in word document but would like a much better version and attached is our logo. Our colors are red, black, and grey. The design does not necessarily have to have all of the bullet points..

Target Market(s)

Golfers, junior high golfers, high school golfers, adult golfers

Font styles to use
Sans Serif

Colors
ec1f27
f04a50
f59296
fbd4d5
aaaaaa
cbcbcb
1b1b1b
474747

Requirements
Nice to have
• Our colors are red, black, and grey, do not have to use all 3 in one design. Also The design does not necessarily have to have all of the bullet points.

```html
<!DOCTYPE html>
<html lang="en">
<head>
<meta charset="utf-8">
<title>Kestrel Golf Circle Chart</title>
<link href="https://fonts.googleapis.com/css2?family=Oswald:wght@500;700&family=Merriweather:wght@400&display=swap" rel="stylesheet">
<style>
  :root {
    --red: #ec1f27;
    --black: #1b1b1b;
    --ink-white: #ffffff;
    --grey-bg: #f3f3f3;
    --grey-line: #474747;
  }
  html, body { margin: 0; padding: 0; overflow: hidden; }
  body { width: 1200px; height: 1200px; background: var(--grey-bg); }
  .process-chart { display: block; width: 1200px; height: 1200px; }
  .ring { fill: var(--red); }
  .orbit { fill: none; stroke: var(--red); stroke-width: 2.5; stroke-dasharray: 2 5; }
  .step-arrow { fill: var(--black); filter: drop-shadow(0 6px 8px rgba(0,0,0,.35)); }
  .step-title { font-family: "Oswald", sans-serif; font-weight: 700; fill: var(--red); }
  .step-item { font-family: "Merriweather", serif; font-size: 15px; fill: var(--ink-white); text-anchor: middle; }
  .brand-name { font-family: "Oswald", sans-serif; font-weight: 700; font-size: 60px; fill: var(--red); text-anchor: middle; }
</style>
</head>
<body>
<svg class="process-chart" viewBox="0 0 1200 1200" xmlns="http://www.w3.org/2000/svg">
  <defs>
    <radialGradient id="ball-shade" cx="40%" cy="35%" r="70%">
      <stop offset="0" stop-color="#ffffff"/>
      <stop offset=".6" stop-color="#eef0f2"/>
      <stop offset="1" stop-color="#c9ccd0"/>
    </radialGradient>
  </defs>

  <circle class="orbit" cx="600" cy="600" r="318"/>
  <circle class="ring" cx="600" cy="600" r="300"/>

  <g class="center-ball" role="img" aria-label="Golf ball illustration">
    <circle cx="600" cy="600" r="225" fill="url(#ball-shade)"/>
  </g>
  <text class="brand-name" x="600" y="622">Kestrel Golf</text>

  <!-- Evaluation -->
  <polygon class="step-arrow" points="300,438 370,220 512,164 502,138 650,188 571,332 588,304"/>
  <text class="step-title" font-size="50" textLength="205" lengthAdjust="spacingAndGlyphs" transform="translate(380,268) rotate(-29)">EVALUATION</text>
  <g class="step-item">
    <text textLength="176" lengthAdjust="spacingAndGlyphs" transform="translate(484,268) rotate(-24)">Video Swing Analysis</text>
    <text textLength="128" lengthAdjust="spacingAndGlyphs" transform="translate(500,290) rotate(-24)">Putting Reports</text>
    <text textLength="130" lengthAdjust="spacingAndGlyphs" transform="translate(514,318) rotate(-24)">Develope a Plan</text>
  </g>

  <!-- Coaching -->
  <polygon class="step-arrow" points="780,316 992,400 1040,544 1064,542 1004,684 862,594 888,584"/>
  <text class="step-title" font-size="52" textLength="164" lengthAdjust="spacingAndGlyphs" transform="translate(822,400) rotate(18)">COACHING</text>
  <g class="step-item">
    <text transform="translate(936,492) rotate(-15)">Tour Quality</text>
    <text transform="translate(942,510) rotate(-15)">Technology</text>
    <text transform="translate(952,538) rotate(-15)">Visualization &amp;</text>
    <text transform="translate(960,556) rotate(-15)">Feedback</text>
    <text transform="translate(966,582) rotate(-15)">Understand</text>
    <text transform="translate(974,600) rotate(-15)">Inconsitencies</text>
  </g>

  <!-- Practice -->
  <polygon class="step-arrow" points="892,760 824,984 692,1040 692,1064 544,1016 616,868 632,888"/>
  <text class="step-title" font-size="54" textLength="164" lengthAdjust="spacingAndGlyphs" transform="translate(636,934) rotate(-21.5)">PRACTICE</text>
  <g class="step-item">
    <text textLength="172" lengthAdjust="spacingAndGlyphs" transform="translate(730,940) rotate(-22)">24/7 Access to Practice</text>
    <text textLength="182" lengthAdjust="spacingAndGlyphs" transform="translate(742,966) rotate(-22)">Practice with a Purpose</text>
  </g>

  <!-- Measure Progress -->
  <polygon class="step-arrow" points="440,896 220,824 164,688 136,692 190,546 336,620 320,636"/>
  <g class="step-title" font-size="54">
    <text textLength="166" lengthAdjust="spacingAndGlyphs" transform="translate(200,752) rotate(15)">MEASURE</text>
    <text textLength="180" lengthAdjust="spacingAndGlyphs" transform="translate(228,816) rotate(17)">PROGRESS</text>
  </g>
  <g class="step-item">
    <text textLength="118" lengthAdjust="spacingAndGlyphs" transform="translate(232,646) rotate(-25)">Track Progress</text>
    <text textLength="74" lengthAdjust="spacingAndGlyphs" transform="translate(242,666) rotate(-25)">with Data</text>
  </g>
</svg>
</body>
</html>
```